redesign laundry perfume webshop

We want to have a custom redesign for our website.
the focus should be luxury design . Please note that our "proefpakket" product is the most sold product.
Hello when desiging. please only use our product fotos, you can edit them, but dont make it look like there are other bottles etc.
Thank you for understanding.
Please dont show in english version (text). Use our language (dutch) use existing text on our website.
Also show our other pages as wel like category and product page etc.
Netherland and belgium
perfume
Coded - Design and coding required
5+ page
Designer to choose colors to be used in the design.

```html
<!DOCTYPE html>
<html lang="nl">
<head>
<meta charset="utf-8">
<title>Linnengloed – Wasparfum</title>
<link href="https://fonts.googleapis.com/css2?family=Playfair+Display:wght@400;700;900&family=Josefin+Sans:wght@300;400;600&family=Mulish:wght@400;600;700&display=swap" rel="stylesheet">
<style>
:root{
  --backdrop:#d5bf98;
  --navy:#232c3d;
  --navy-line:#36415a;
  --gold:#d8a840;
  --gold-soft:#e6bf66;
  --paper:#f3f2f0;
  --white:#ffffff;
  --ink:#2b2b2b;
  --muted:#6a6a6a;
  --cream:#f6ecdc;
}
*{box-sizing:border-box;margin:0;padding:0}
html,body{width:1200px;height:3125px;overflow:hidden}
body{background:var(--backdrop);font-family:"Mulish",sans-serif;color:var(--ink)}
.page{position:absolute;left:146px;top:70px;width:908px;height:2987px;background:var(--white);box-shadow:0 6px 30px rgba(0,0,0,.18);overflow:hidden}
section,header,footer{position:relative;width:100%}
.serif{font-family:"Playfair Display",serif}

/* hero */
.hero{height:440px;background:var(--navy)}
.topbar{height:17px;border-bottom:1px solid var(--navy-line);text-align:center;font-size:8px;color:var(--gold);line-height:17px;font-family:"Josefin Sans",sans-serif}
.brand{position:absolute;left:115px;top:26px;width:70px;text-align:center;color:var(--gold);font-family:"Playfair Display",serif;font-size:10px;letter-spacing:.5px}
.brand .dot{display:block;width:30px;height:30px;border:2px solid var(--gold);border-radius:50%;margin:0 auto 5px}
.nav{position:absolute;left:312px;top:26px;display:flex;gap:18px;font-size:8.5px;color:#fff;font-family:"Josefin Sans",sans-serif;z-index:2}
.nav-icons{position:absolute;left:745px;top:24px;display:flex;gap:14px;z-index:2}
.hero-photo{position:absolute;left:353px;top:18px;width:555px;height:422px;background:radial-gradient(ellipse at 60% 40%,#f1ddd3 0%,#c99a90 35%,#5a5c66 70%,#2c3444 100%)}
.hero-copy{position:absolute;left:117px;top:170px;z-index:2}
.hero-kicker{font-family:"Josefin Sans",sans-serif;color:var(--gold);font-size:22px;font-weight:300}
.hero-title{font-family:"Playfair Display",serif;font-weight:900;color:#fff;font-size:58px;letter-spacing:2px;line-height:1.05}
.hero-sub{color:#fff;font-size:11px;margin-left:18px;font-family:"Josefin Sans",sans-serif}
.tv{display:flex;align-items:center;gap:8px;margin:36px 0 0 18px;color:#fff;font-size:8.5px;font-weight:700}
.tv-badge{width:24px;height:24px;background:var(--gold);border-radius:3px}

/* usp */
.usp{height:135px;background:var(--paper);display:flex;justify-content:center;align-items:center;gap:22px}
.usp-item{text-align:center;font-family:"Josefin Sans",sans-serif;font-size:13px;color:#333;width:125px}
.usp-icon{width:42px;height:42px;border:2px solid var(--gold);border-radius:50%;margin:0 auto 12px}
.usp-sep{width:1px;height:70px;background:#d7d2c8}

/* products */
.shop{height:574px;padding:15px 0 0 13px;background:var(--white)}
.grid{display:grid;grid-template-columns:repeat(3,285px);grid-auto-rows:266px;gap:14px 15px}
.card{position:relative;background:var(--paper);text-align:center}
.card .ribbon{position:absolute;left:-4px;top:5px;background:var(--gold);color:#fff;font-size:8px;font-weight:700;padding:3px 10px 3px 6px}
.product-shot{margin:18px auto 0;width:56px;height:112px;border-radius:8px 8px 4px 4px}
.product-shot.wide{width:190px;border-radius:4px;background:linear-gradient(#3a2517 0 35%,#e3a04a 35% 100%)}
.p-name{font-family:"Playfair Display",serif;font-weight:700;font-size:13px;letter-spacing:.5px;margin-top:10px}
.rating{font-size:7.5px;color:var(--muted);margin-top:3px}
.rating b{color:var(--gold);letter-spacing:1px}
.price{font-size:15px;margin-top:14px;letter-spacing:.5px}
.price s{color:#999;margin-right:8px}
.card-foot{position:absolute;left:27px;right:20px;bottom:22px;display:flex;justify-content:space-between;align-items:center}
.ship{font-size:8px;text-align:center;line-height:1.4}
.ship b{display:block}
.btn{display:inline-block;border:1.5px solid var(--gold);color:var(--gold);font-size:8px;padding:6px 14px;background:#fff}

/* about */
.about{height:348px;display:flex}
.about-text{position:relative;z-index:2;width:455px;flex:none;padding:52px 30px 0 120px}
.about-text h2{position:relative;z-index:3;font-family:"Playfair Display",serif;font-size:18.5px;line-height:1.4;width:420px;letter-spacing:.5px}
.about-text p{font-size:7.6px;line-height:2.25;color:#444;margin:16px 0 12px;width:305px}
.about-photo{position:relative;z-index:1;width:453px;flex:none;background:linear-gradient(100deg,#ececec 0%,#dcdcdc 45%,#b9c5d4 75%,#e8e8e8 100%)}

/* video row */
.howto{height:301px;display:flex}
.video{position:relative;width:453px;background:linear-gradient(#c6504a 0 16%,#d8d8d8 16% 82%,#b0b0b0 82%)}
.play{position:absolute;left:210px;top:134px;width:34px;height:34px;border-radius:50%;background:var(--gold)}
.steps{padding:40px 100px 0 48px;list-style:none}
.steps li{display:flex;gap:8px;font-size:7.6px;line-height:2.2;color:#444;margin-bottom:17px}
.steps svg{flex:none;margin-top:4px}

/* sample pack */
.sample{height:392px;background:radial-gradient(ellipse at 35% 55%,#fbf5ea 0%,var(--cream) 45%,#efe0c6 100%)}
.sample h2{position:absolute;left:0;right:0;top:62px;text-align:center;font-family:"Playfair Display",serif;font-size:19px;letter-spacing:.5px}
.sample-shot{position:absolute;left:258px;top:170px;width:164px;height:125px;border-radius:4px;background:linear-gradient(#3a2517 0 40%,#e3a04a 40%)}
.sample-text{position:absolute;left:493px;top:160px;width:232px}
.sample-text p{font-size:7.6px;line-height:2.25;color:#444;margin-bottom:14px}

/* reviews */
.reviews{height:330px;background:var(--paper)}
.reviews h2{position:absolute;left:0;right:0;top:50px;text-align:center;font-family:"Playfair Display",serif;font-size:19px;letter-spacing:.5px}
.ghost{position:absolute;top:128px;width:60px;height:122px;background:#fff;display:flex;align-items:center;justify-content:center;color:#ccc;font-size:26px;font-weight:300}
.review{position:absolute;left:234px;top:115px;width:441px;height:150px;background:#fff;box-shadow:0 3px 14px rgba(0,0,0,.08);padding:22px 20px 0 30px}
.quote-mark{position:absolute;left:14px;top:-12px;font-family:"Playfair Display",serif;color:var(--gold);font-size:48px;line-height:1}
.review p{font-size:7.6px;line-height:2.2;color:#444}
.author{display:flex;align-items:center;gap:10px;margin-top:12px;font-size:8px}
.avatar{width:30px;height:30px;border-radius:50%;background:#b79a86}
.author small{display:block;color:var(--gold);font-size:6.5px}

/* newsletter */
.newsletter{height:131px;background:#fff}
.nl-copy{position:absolute;left:120px;top:36px}
.nl-copy h3{font-family:"Playfair Display",serif;font-size:18px;letter-spacing:.5px}
.nl-copy p{font-size:9.5px;line-height:1.55;margin-top:3px;width:310px}
.nl-input{position:absolute;left:461px;top:46px;width:214px;height:29px;border:1px solid #e2e2e2;background:#f7f7f7;font-size:7.5px;color:#999;padding:10px}
.nl-btn{position:absolute;left:688px;top:46px;width:100px;height:29px;background:var(--gold);color:#fff;font-size:8px;font-weight:700;text-align:center;line-height:29px}

/* footer */
.footer{height:336px;background:var(--navy);color:#fff}
.footer .brand{left:419px;top:-22px;width:70px}
.footer .brand .dot{background:var(--navy)}
.cols{position:absolute;left:120px;top:78px;display:grid;grid-template-columns:170px 170px 170px 170px}
.cols h4{font-size:8.5px;letter-spacing:.8px;font-weight:700;margin-bottom:12px}
.cols li{list-style:none;font-size:7px;line-height:2.55;color:#dfe2e8}
.contact li{display:flex;gap:6px;align-items:flex-start;margin-bottom:4px;line-height:1.9}
.socials{display:flex;gap:4px;margin-top:6px}
.socials span{width:15px;height:15px;border-radius:50%;background:var(--gold)}
.legal{position:absolute;left:120px;right:120px;top:264px;border-top:1px solid var(--navy-line);padding-top:16px;text-align:center;font-size:6.5px;color:#dfe2e8}
.legal em{font-style:normal;color:var(--gold)}
.pay{display:flex;justify-content:center;gap:4px;margin-top:9px}
.pay span{width:23px;height:14px;border-radius:2px;background:#e8e8e8}
</style>
</head>
<body>
<div class="page">

  <header class="hero">
    <div class="topbar">Gratis verzending NL &amp; BE</div>
    <div class="hero-photo" role="img" aria-label="Foto van een vrouw die met gesloten ogen aan een roze, frisgewassen laken ruikt"></div>
    <div class="brand"><span class="dot"></span>LINNENGLOED</div>
    <nav class="nav"><span>Thuis</span><span>Wasparfum</span><span>Verkooppunten</span><span>Waarom linnengloed</span><span>Contact</span></nav>
    <div class="nav-icons">
      <svg width="10" height="10" viewBox="0 0 10 10"><circle cx="5" cy="5" r="4" fill="none" stroke="#fff" stroke-width="1"/><circle cx="5" cy="4" r="1.5" fill="none" stroke="#fff"/></svg>
      <svg width="12" height="12" viewBox="0 0 12 12"><rect x="1.5" y="3.5" width="8" height="7" fill="none" stroke="#fff"/><circle cx="10" cy="2" r="2" fill="#d8a840"/></svg>
    </div>
    <div class="hero-copy">
      <div class="hero-kicker">Muffe was is nu verleden tijd!</div>
      <div class="hero-title">LINNENGLOED</div>
      <div class="hero-sub">Ieder dag weer een glimlach.</div>
      <div class="tv">Bekend van TV! <span class="tv-badge"></span></div>
    </div>
  </header>

  <section class="usp">
    <div class="usp-item"><div class="usp-icon"></div>Geen parabenen</div>
    <div class="usp-sep"></div>
    <div class="usp-item"><div class="usp-icon"></div>Gerecycled plastic</div>
  </section>

  <section class="shop">
    <div class="grid">
      <article class="card">
        <span class="ribbon">Aanbieding!</span>
        <div class="product-shot wide" role="img" aria-label="Productfoto cadeauset wasparfum"></div>
        <h3 class="p-name">CADEAUSET WASPARFUM</h3>
        <div class="rating"><b>★★★★★</b> (718 Recensies)</div>
        <div class="price"><s>89.70</s>74.95</div>
        <div class="card-foot"><div class="ship"><b>Vandaag Verzonden</b>voor 16:00 besteld</div><span class="btn">🛍 Toevoegen aan winkelwagen</span></div>
      </article>
      <article class="card">
        <div class="product-shot" style="background:linear-gradient(#f4f4f4 0 22%,#bcd6ee 22%)" role="img" aria-label="Productfoto fles Petal Shower"></div>
        <h3 class="p-name">PETAL SHOWER</h3>
        <div class="rating"><b>★★★★★</b> (718 Recensies)</div>
        <div class="price">14.95</div>
        <div class="card-foot"><div class="ship"><b>Vandaag Verzonden</b>voor 16:00 besteld</div><span class="btn">🛍 Toevoegen aan winkelwagen</span></div>
      </article>
      <article class="card">
        <div class="product-shot" style="background:linear-gradient(#f4f4f4 0 22%,#3b3a86 22%)" role="img" aria-label="Productfoto fles Night Bloom"></div>
        <h3 class="p-name">NIGHT BLOOM</h3>
        <div class="rating"><b>★★★★★</b> (718 Recensies)</div>
        <div class="price">14.95</div>
        <div class="card-foot"><div class="ship"><b>Vandaag Verzonden</b>voor 16:00 besteld</div><span class="btn">🛍 Toevoegen aan winkelwagen</span></div>
      </article>
      <article class="card">
        <div class="product-shot" style="background:linear-gradient(#f4f4f4 0 22%,#d8595c 22%)" role="img" aria-label="Productfoto fles Dawn Mist"></div>
        <h3 class="p-name">DAWN MIST</h3>
        <div class="rating"><b>★★★★★</b> (718 Recensies)</div>
        <div class="price">14.95</div>
        <div class="card-foot"><div class="ship"><b>Vandaag Verzonden</b>voor 16:00 besteld</div><span class="btn">🛍 Toevoegen aan winkelwagen</span></div>
      </article>
      <article class="card">
        <div class="product-shot" style="background:linear-gradient(#f4f4f4 0 22%,#8fbde3 22%)" role="img" aria-label="Productfoto fles Bloom Dew"></div>
        <h3 class="p-name">BLOOM DEW</h3>
        <div class="rating"><b>★★★★★</b> (718 Recensies)</div>
        <div class="price">14.95</div>
        <div class="card-foot"><div class="ship"><b>Vandaag Verzonden</b>voor 16:00 besteld</div><span class="btn">🛍 Toevoegen aan winkelwagen</span></div>
      </article>
      <article class="card">
        <div class="product-shot" style="background:linear-gradient(#f4f4f4 0 22%,#ef9a2a 22%)" role="img" aria-label="Productfoto fles Sunglow"></div>
        <h3 class="p-name">SUNGLOW</h3>
        <div class="rating"><b>★★★★★</b> (718 Recensies)</div>
        <div class="price">14.95</div>
        <div class="card-foot"><div class="ship"><b>Vandaag Verzonden</b>voor 16:00 besteld</div><span class="btn">🛍 Toevoegen aan winkelwagen</span></div>
      </article>
    </div>
  </section>

  <section class="about">
    <div class="about-text">
      <h2>Linnengloed heerlijke, luxe, milieubewuste en langdurige geur voor uw wasgoed.</h2>
      <p>Linnengloed, de nieuwste Italiaanse wassensatie nu ook in Nederland. Onze Italiaanse luxe wasparfums geven jouw wasgoed een langdurige geurboost. Heerlijk ruikende was in plaats van een muffe geur. Linnengloed komt rechtstreeks uit Italië, is milieubewust en kindvriendelijk. Onze frisse en delicate wasgeuren zijn parabenen vrij (E-nummers) en gemaakt op basis van etherische oliën. Onze heerlijke geuren worden aan het eind van uw wasprogramma vermengd met het wasgoed. Omdat het etherische oliën zijn, blijven onze geuren dus extra lang hangen. Hierdoor wordt ook nog eens de omgeving waarin u de was opruimt geurig. Linnengloed zorgt ervoor dat u iedere wasdag begint en eindigt met een vrolijke glimlach.</p>
      <span class="btn" style="padding:6px 30px">Veel gestelde vragen ›</span>
    </div>
    <div class="about-photo" role="img" aria-label="Foto van een lachende vrouw naast een kledingrek met overhemden"></div>
  </section>

  <section class="howto">
    <div class="video" role="img" aria-label="Uitlegvideo: getekende waslijn met kleding onder een dakrand">
      <svg class="play" viewBox="0 0 34 34"><circle cx="17" cy="17" r="17" fill="#d8a840"/><path d="M13 10 L24 17 L13 24 Z" fill="#fff"/></svg>
    </div>
    <ul class="steps">
      <li><svg width="9" height="9" viewBox="0 0 9 9"><circle cx="4.5" cy="4.5" r="4" fill="none" stroke="#d8a840"/><path d="M2.5 4.6 4 6 6.6 3" fill="none" stroke="#d8a840"/></svg>Linnengloed zorgt ervoor dat je was langer lekker ruikt.</li>
      <li><svg width="9" height="9" viewBox="0 0 9 9"><circle cx="4.5" cy="4.5" r="4" fill="none" stroke="#d8a840"/><path d="M2.5 4.6 4 6 6.6 3" fill="none" stroke="#d8a840"/></svg>Hoe gebruik je onze 100ml Linnengloed? – Druppel de wasparfum (2.5ml tot 5ml) doe de vloeibare Wasparfum in het laatje van de wasverzachter bij een volle wastrommel.</li>
      <li><svg width="9" height="9" viewBox="0 0 9 9"><circle cx="4.5" cy="4.5" r="4" fill="none" stroke="#d8a840"/><path d="M2.5 4.6 4 6 6.6 3" fill="none" stroke="#d8a840"/></svg>Hoe gebruik je ons proefpakket? – Druppel minimaal een half flesje van uw proefpakket (2.5ml tot 5ml) wasparfum in het laatje van de wasverzachter bij een volle wastrommel.</li>
      <li><svg width="9" height="9" viewBox="0 0 9 9"><circle cx="4.5" cy="4.5" r="4" fill="none" stroke="#d8a840"/><path d="M2.5 4.6 4 6 6.6 3" fill="none" stroke="#d8a840"/></svg>Linnengloed is een extra toevoeging naast je bestaande wasmiddel &amp; wasverzachter. Wij adviseren neutrale/geurloze wasmiddel te gebruiken.</li>
    </ul>
  </section>

  <section class="sample" role="region" aria-label="Proefpakket op een achtergrond van gedrapeerde crèmekleurige stof">
    <h2>Proefpakket Linnengloed</h2>
    <div class="sample-shot" role="img" aria-label="Productfoto proefpakket met vijf flesjes"></div>
    <div class="sample-text">
      <p>Ons klein maar al zo fijne proefpakket geeft u de mogelijkheid om kennis te maken met onze lijn van vijf wasgeuren. U hoeft enkel en alleen de kindveilige dopjes los te draaien en de inhoud in het wasverzachterbakje leeg te gieten. Na het draaien van uw wasprogramma en vervolgens het openen van uw asmachinedeur zullen u en uw omgeving direct ontdekken wat uw favoriete wasgeur(en) zal zijn. (wordt tijdelijk in een andere verpakking geleverd)</p>
      <span class="btn" style="padding:6px 28px">Bestel hier proefpakket</span>
    </div>
  </section>

  <section class="reviews">
    <h2>Onze blije klanten aan het woord</h2>
    <div class="ghost" style="left:178px">‹</div>
    <div class="ghost" style="left:670px">›</div>
    <div class="review">
      <span class="quote-mark">“</span>
      <p>Wat ben ik gelukkig met deze geurtjes! Mijn vriend en ik zijn heel gevoelig als het op geur aankomt. Wij worden snel onpasselijk van luchtjes, maar als het de juiste zijn worden wij heel blij. Wat ben ik blij dat ik jullie ontdekt heb. Ik ben nog met het proefpakket bezig, maar ik weet nu al dat ik dit voortaan ga gebruiken. Echt zo lekker!</p>
      <div class="author"><span class="avatar"></span><div><b>Marloes de Vries</b><small>Klant ervaring sociale media</small></div></div>
    </div>
  </section>

  <section class="newsletter">
    <div class="nl-copy"><h3>Aanmelden voor nieuwsbrief?</h3><p>U wordt maandelijks op de hoogte gehouden van kortingen en nieuwste producten!</p></div>
    <div class="nl-input">E-mailadres</div>
    <div class="nl-btn">Aanmelden</div>
  </section>

  <footer class="footer">
    <div class="brand"><span class="dot"></span>LINNENGLOED</div>
    <div class="cols">
      <div>
        <h4>CONTACT</h4>
        <ul class="contact">
          <li><svg width="8" height="10" viewBox="0 0 8 10"><path d="M4 9.5C1.5 6 .5 4.6.5 3.5a3.5 3.5 0 0 1 7 0C7.5 4.6 6.5 6 4 9.5Z" fill="none" stroke="#fff" stroke-width=".8"/></svg>Voorbeeldstraat 12,<br>1000 AA, Amsterdam</li>
          <li><svg width="9" height="9" viewBox="0 0 9 9"><path d="M1 1.5 3 1 4 3 3 4a5 5 0 0 0 2 2l1-1 2 1-.5 2C4 8 1 5 1 1.5Z" fill="none" stroke="#fff" stroke-width=".8"/></svg>+31200000000</li>
          <li><svg width="10" height="8" viewBox="0 0 10 8"><rect x=".5" y=".5" width="9" height="7" fill="none" stroke="#fff" stroke-width=".8"/><path d="M.5 .5 5 4.5 9.5 .5" fill="none" stroke="#fff" stroke-width=".8"/></svg>info@linnengloed.nl</li>
        </ul>
        <div class="socials"><span></span><span></span><span></span><span></span></div>
      </div>
      <div>
        <h4>INFORMATIE</h4>
        <ul><li>Veel gestelde vragen</li><li>Klantenervaring</li><li>Betaalmogelijkheden</li><li>Verzenden en retourneren</li></ul>
      </div>
      <div>
        <h4>SNELLE LINKS</h4>
        <ul><li>Wasparfum proefpakket</li><li>Verkooppunten</li><li>Verkooppunt worden?</li><li>Blogs</li><li>contact ons</li><li>Algemene voorwaarden</li><li>Onze Wasparfums</li></ul>
      </div>
      <div>
        <h4>BEREIKBARE TIJDEN</h4>
        <ul><li>dinsdag t/m vrijdag</li><li>11:00 - 17:00</li></ul>
      </div>
    </div>
    <div class="legal">
      © 2023 <em>Linnengloed</em> Alle rechten voorbehouden &nbsp;|&nbsp; Privacy Policy &nbsp;|&nbsp; Algemene voorwaarden
      <div class="pay"><span></span><span></span><span></span><span></span><span></span></div>
    </div>
  </footer>

</div>
</body>
</html>
```